Brochure update and matching sign-up form

We are a high end Tanning Salon that offers multiple levels of Tanning, Red Light, Sunless, and Hybrid (UV and Red Light in a single session).

I want to modernize our current brochure (the original is included in the links below, along with some changes to it), and add a sign-up form for new clients that helps guide them through the purchasing process.

I want the sign-up form to be 11 x 17 double sided, with the demographics and purchasing information on one side, and the waiver/terms on the back side. This form needs to be super clean and easy to fill out, and should lead the client through the sign-up and purchasing options. Without knowing how this might look or how much space it will take, I do anticipate revisions after the first draft.

The information provided in the links isn't formatted as good as I would normally like, but you'll obviously keep the layout consistent. There will be some images needed after the first draft.

Once done, I will probably need these in various formats (print and digital) with any necessary revisions to accommodate the various formats and uses.

See links:

Brochure Revisions: https://www.quillraft.com/shard/s72/sh/a3d9e712-c4f0-19ab-b6e2-7c05d1a9e48f/TkRmWobv3ZqHs8NeL2xcJyfuGdPa4VtiQ_7kLmRzXwbOyhUnCe-5s2Dp

Sign-up form: https://www.quillraft.com/shard/s72/sh/2e7b9f30-d5a1-4c8e-93fb-6a10c47e8d25/hrTqZvoe3MmNbW8yKd1_PsjuLx7GaRi49XnEc625JQV_Hz3wCkUa4F8peB

```html
<!DOCTYPE html>
<html lang="en">
<head>
<meta charset="utf-8">
<title>SolHaven Pricing Brochure</title>
<link href="https://fonts.googleapis.com/css2?family=Exo+2:wght@500;600;700&family=Didact+Gothic&display=swap" rel="stylesheet">
<style>
:root{
  --sun:#fdd24d;
  --navy:#0f4470;
  --ink:#17375c;
  --body:#111;
  --white:#fff;
  --blue:#1565b0;
}
*{box-sizing:border-box;margin:0;padding:0}
html,body{width:1200px;height:783px;overflow:hidden;background:var(--white)}
body{font-family:"Didact Gothic",sans-serif;color:var(--body);position:relative}
.abs{position:absolute}
.title-bar{display:flex;height:39px}
.title-bar .num{background:var(--sun);color:var(--navy);width:39px;display:flex;align-items:center;justify-content:center;font:700 30px "Exo 2",sans-serif}
.title-bar .text{background:var(--navy);color:var(--sun);font:600 14px/17px "Exo 2",sans-serif;padding:3px 6px;letter-spacing:.3px}
.col-head{font-size:7px;line-height:8px;color:var(--ink)}
.col-head b{font-family:"Exo 2",sans-serif;font-weight:700;font-size:6px}
.col-head small{font-size:4.5px;display:block}
.cell{position:absolute;background:var(--sun);width:42px;color:var(--ink);display:flex;flex-direction:column;align-items:center;justify-content:center;text-align:center}
.amt{font:700 13.5px "Exo 2",sans-serif;color:var(--ink)}
.amt sup{font-size:7px;vertical-align:5px}
.note{font-size:4.5px;line-height:5px}
.rule{width:30px;border-top:.6px solid var(--ink);margin:1px 0}
.upgrade{position:absolute;border-top:.7px solid var(--ink);text-align:center;color:var(--ink);font-size:8px;line-height:9px}
.upgrade .amt{font-size:12px}
.c1{left:247px}.c2{left:299px}.c3{left:350px}.c4{left:398px}.c5{left:447px}.c6{left:496px}.c7{left:545px}
.r1{left:828px}.r2{left:880px}.r3{left:930px}.r4{left:980px}.r5{left:1028px}.r6{left:1077px}.r7{left:1126px}
.level{position:absolute;left:44px;display:flex;align-items:center}
.level .badge{background:var(--sun);color:var(--navy);font:700 18px "Exo 2",sans-serif;width:21px;height:21px;display:flex;align-items:center;justify-content:center}
.level .arrow{width:0;height:0;border-top:10.5px solid transparent;border-bottom:10.5px solid transparent;border-left:9px solid var(--sun)}
.photo{position:absolute;border-radius:4px}
.photo.bed{background:linear-gradient(180deg,#cfe6f7,#7aa7c8 60%,#e9eef2)}
.photo.booth-pink{background:linear-gradient(90deg,#f6d6e4,#e98fb6,#f6d6e4);border-radius:6px}
.photo.booth-red{background:linear-gradient(90deg,#2b2b2b,#c4261f,#2b2b2b);border-radius:6px}
.photo.bottle{background:linear-gradient(180deg,#eee,#555);border-radius:3px}
.photo.bottle-dark{background:linear-gradient(180deg,#666,#111);border-radius:3px}
.photo.bottle-green{background:linear-gradient(180deg,#eef5e4,#a9cf8c);border-radius:5px}
.cap{position:absolute;font-size:8px;color:var(--navy)}
.desc{position:absolute;font-size:7.4px;line-height:8.1px;text-align:justify;color:var(--body)}
.desc.rec{font-size:7.8px;line-height:9.3px}
.tag{position:absolute;display:flex;align-items:center}
.tag .t{background:var(--sun);color:var(--navy);font:700 16px/22px "Exo 2",sans-serif;padding:0 4px;height:22px}
.tag .arrow{width:0;height:0;border-top:11px solid transparent;border-bottom:11px solid transparent;border-left:9px solid var(--sun)}
.navy-tab{position:absolute;background:var(--navy);color:var(--sun);font:700 15px "Exo 2",sans-serif;display:flex;align-items:center;justify-content:center;letter-spacing:.5px}
.list{position:absolute;font-size:8.2px;line-height:10.5px;color:var(--body)}
.list li{margin-left:17px}
.freedom{position:absolute;background:var(--sun);height:58px}
.freedom .circle{position:absolute;left:-13px;top:-3px;width:56px;height:56px;border-radius:50%;background:var(--navy);border:3px solid var(--sun);color:var(--sun);font:700 30px "Exo 2",sans-serif;display:flex;align-items:center;justify-content:center}
.freedom .name{position:absolute;left:46px;top:2px;font:700 11px "Exo 2",sans-serif;color:var(--navy)}
.freedom .price{position:absolute;left:54px;top:16px;font:700 20px "Exo 2",sans-serif;color:var(--navy)}
.freedom .price sup{font-size:10px;vertical-align:8px}
.freedom .pm{position:absolute;left:52px;top:41px;font-size:8px;color:var(--navy)}
.save-box{position:absolute;background:var(--navy)}
.ribbon{position:absolute;background:var(--sun);color:var(--navy);font:700 9px/18px "Exo 2",sans-serif;text-align:center;height:18px}
.deal{position:absolute;background:var(--white);top:20px;width:52px;height:58px;color:var(--navy);padding:2px 3px;font-family:"Exo 2",sans-serif;font-weight:700;font-size:9px;line-height:9px}
.deal small{font-size:5px;font-weight:500;display:block;line-height:6px}
.deal .pct{position:absolute;left:0;right:0;bottom:0;background:var(--sun);text-align:center;font-size:10px;line-height:9px;padding:1px 0}
.deal .pct small{font-size:6px;line-height:6px}
.gift{position:absolute;background:var(--blue);color:var(--sun);font:600 9px/10px "Exo 2",sans-serif;text-align:center;display:flex;align-items:center;justify-content:center}
.gift.white{color:var(--white)}
.rec-head{position:absolute;font:700 12px/15px "Exo 2",sans-serif;color:var(--navy)}
.terms{position:absolute;left:0;top:703px;width:602px;height:59px;background:var(--navy);color:var(--sun);font-size:8.3px;line-height:9.3px;padding:7px 10px 0 50px}
</style>
</head>
<body>

<!-- LEFT: UV levels -->
<div class="abs title-bar" style="left:42px;top:24px;width:260px">
  <div class="num">5</div>
  <div class="text">Levels of UV tanning, Sunless,<br>Hybrid &amp; Red Light</div>
</div>

<div class="abs col-head" style="left:44px;top:79px;font-size:9.5px">Level</div>
<div class="abs col-head" style="left:127px;top:77px;font-size:9.5px">Equipment</div>
<div class="abs col-head" style="left:247px;top:70px">Best<br>Monthly Rate<br>When paid<br>annualy</div>
<div class="abs col-head" style="left:299px;top:78px">Monthly<br>Auto-Pay<br>Committment</div>
<div class="abs col-head" style="left:350px;top:78px">Monthly<br>Auto-Pay<br>Flex</div>
<div class="abs col-head" style="left:398px;top:87px">30 Day<br>Unlimited</div>
<div class="abs col-head" style="left:447px;top:87px">Single<br>Visit</div>
<div class="abs col-head" style="left:496px;top:80px"><b>Buy 5,<br>Get 2 FREE</b><small>Valid for 365 days</small></div>
<div class="abs col-head" style="left:545px;top:80px"><b>Buy 10,<br>Get 5 FREE</b><small>Valid for 365 days</small></div>

<!-- Level 1 -->
<div class="level" style="top:99px"><div class="badge">1</div><div class="arrow"></div></div>
<div class="photo bed" role="img" aria-label="Level 1 lay-down tanning bed" style="left:118px;top:95px;width:72px;height:40px"></div>
<div class="cap" style="left:92px;top:133px">Sunridge</div>
<div class="desc" style="left:44px;top:148px;width:196px;text-align:left">28 lamps and a 500 watt facial tanner in a 20 minute maximum session</div>

<div class="cell c1" style="top:105px;height:57px"><span class="amt"><sup>$</sup>29</span><span class="note">per month</span><div class="rule"></div><span class="amt" style="font-size:10px"><sup>$</sup>345</span><span class="note">annualy</span></div>
<div class="cell c2" style="top:105px;height:57px"><span class="amt"><sup>$</sup>33<sup>88</sup></span></div>
<div class="cell c3" style="top:105px;height:57px"><span class="amt"><sup>$</sup>37<sup>88</sup></span></div>
<div class="cell c4" style="top:105px;height:57px"><span class="amt"><sup>$</sup>75</span></div>
<div class="cell c5" style="top:105px;height:57px"><span class="amt"><sup>$</sup>13</span></div>
<div class="cell c6" style="top:105px;height:57px"><span class="amt"><sup>$</sup>65</span></div>
<div class="cell c7" style="top:105px;height:57px"><span class="amt"><sup>$</sup>130</span><div class="rule"></div><span class="amt" style="font-size:9px"><sup>$</sup>8<sup>66</sup></span><span class="note">for each</span></div>

<!-- Levels 2 & 3 -->
<div class="level" style="top:171px"><div class="badge">2</div><div class="arrow"></div></div>
<div class="photo bed" role="img" aria-label="Level 2 lay-down tanning bed" style="left:123px;top:170px;width:58px;height:34px"></div>
<div class="cap" style="left:106px;top:194px">Klarion</div>
<div class="level" style="top:220px"><div class="badge">3</div><div class="arrow"></div></div>
<div class="photo bed" role="img" aria-label="Level 3 tanning bed" style="left:82px;top:212px;width:44px;height:30px"></div>
<div class="photo bed" role="img" aria-label="Leg tanning unit" style="left:136px;top:205px;width:44px;height:38px"></div>
<div class="photo booth-red" role="img" aria-label="Stand-up tanning booth" style="left:197px;top:195px;width:24px;height:44px;background:linear-gradient(90deg,#111,#2a4fa6,#111)"></div>
<div class="cap" style="left:85px;top:246px">Ardent</div>
<div class="cap" style="left:133px;top:246px">Leg Tanner</div>
<div class="cap" style="left:183px;top:240px;line-height:9px">Super Vortex<br>stand-up</div>
<div class="desc" style="left:44px;top:262px;width:188px">More lamps for better body coverage, and triple the face tanning power, makes these laydowns the most powerfull you'll find in a 20 minute lamp format includes stand-up for more tan building UVA a faster session and complete 360 coverage</div>

<div class="cell c1" style="top:167px;height:138px"><span class="amt"><sup>$</sup>39</span><span class="note">per month</span><div class="rule"></div><span class="amt" style="font-size:10px"><sup>$</sup>465</span><span class="note">annualy</span></div>
<div class="cell c2" style="top:167px;height:138px;justify-content:flex-start;padding-top:58px"><span class="amt"><sup>$</sup>45<sup>88</sup></span></div>
<div class="cell c3" style="top:167px;height:138px;justify-content:flex-start;padding-top:58px"><span class="amt"><sup>$</sup>58<sup>88</sup></span></div>
<div class="abs" style="left:299px;top:280px;width:92px;height:25px;background:var(--sun)"></div>
<div class="upgrade" style="left:299px;top:280px;width:92px;padding-top:2px">Memeber Upgrade<br><span class="amt"><sup>$</sup>5</span></div>
<div class="cell c4" style="top:167px;height:138px"><span class="amt"><sup>$</sup>95</span></div>
<div class="cell c5" style="top:167px;height:138px"><span class="amt"><sup>$</sup>18</span></div>
<div class="cell c6" style="top:167px;height:138px"><span class="amt"><sup>$</sup>90</span></div>
<div class="cell c7" style="top:167px;height:138px"><span class="amt"><sup>$</sup>180</span><div class="rule"></div><span class="amt" style="font-size:9px"><sup>$</sup>12</span><span class="note">for each</span></div>

<!-- Level 4 -->
<div class="level" style="top:312px"><div class="badge">4</div><div class="arrow"></div></div>
<div class="photo booth-red" role="img" aria-label="Level 4 stand-up booth" style="left:89px;top:309px;width:22px;height:42px;background:linear-gradient(90deg,#3a2a5a,#f3c33b,#3a2a5a)"></div>
<div class="photo bed" role="img" aria-label="Level 4 lay-down tanning bed" style="left:139px;top:312px;width:61px;height:36px"></div>
<div class="cap" style="left:85px;top:353px">Vela 250</div>
<div class="cap" style="left:148px;top:353px">Aurora 500</div>
<div class="desc" style="left:46px;top:366px;width:193px">All level 4+ beds have more lamps. 3x the UVA (the tanning rays) and much quicker tanning times then lower levels. They provide 360 degree coverage and are loaded with comfort features such as variable control cooling contoured plexi, shoulder tanners and more.</div>

<div class="cell c1" style="top:317px;height:70px"><span class="amt"><sup>$</sup>49</span><span class="note">per month</span><div class="rule"></div><span class="amt" style="font-size:10px"><sup>$</sup>599</span><span class="note">annualy</span></div>
<div class="cell c2" style="top:317px;height:70px;justify-content:flex-start;padding-top:14px"><span class="amt"><sup>$</sup>56<sup>88</sup></span></div>
<div class="cell c3" style="top:317px;height:70px;justify-content:flex-start;padding-top:14px"><span class="amt"><sup>$</sup>69<sup>88</sup></span></div>
<div class="abs" style="left:299px;top:360px;width:92px;height:27px;background:var(--sun)"></div>
<div class="upgrade" style="left:299px;top:360px;width:92px;padding-top:2px">Memeber Upgrade<br><span class="amt"><sup>$</sup>10</span></div>
<div class="cell c4" style="top:317px;height:70px"><span class="amt"><sup>$</sup>125</span></div>
<div class="cell c5" style="top:317px;height:70px"><span class="amt"><sup>$</sup>22</span></div>
<div class="cell c6" style="top:317px;height:70px"><span class="amt"><sup>$</sup>110</span></div>
<div class="cell c7" style="top:317px;height:70px"><span class="amt"><sup>$</sup>180</span><div class="rule"></div><span class="amt" style="font-size:9px"><sup>$</sup>12</span><span class="note">for each</span></div>

<!-- Level 5 -->
<div class="level" style="top:424px"><div class="badge">5</div><div class="arrow"></div></div>
<div class="photo bed" role="img" aria-label="Level 5 high-pressure tanning bed" style="left:86px;top:416px;width:63px;height:52px;background:linear-gradient(180deg,#9bb3c7,#3f5568)"></div>
<div class="photo bed" role="img" aria-label="Level 5 luxury tanning bed" style="left:168px;top:414px;width:70px;height:54px"></div>
<div class="cap" style="left:107px;top:470px">Regalia</div>
<div class="cap" style="left:176px;top:470px">High Pressure</div>
<div class="desc" style="left:46px;top:484px;width:193px">The highest end tanning units in the world. Enjoy true High Pressure tanning for the deepest and darkest tan possible with little to no risk of burning and a tan that lasts 3.5 times longer than conventional bed. Or try luxury packed conventional beds with real a/c personal music systems, aromatherapy misters and amazingly fast session times of just 4-10 minutes.</div>

<div class="cell c1" style="top:417px;height:70px"><span class="amt"><sup>$</sup>66</span><span class="note">per month</span><div class="rule"></div><span class="amt" style="font-size:10px"><sup>$</sup>799</span><span class="note">annualy</span></div>
<div class="cell c2" style="top:417px;height:70px;justify-content:flex-start;padding-top:14px"><span class="amt"><sup>$</sup>76<sup>88</sup></span></div>
<div class="cell c3" style="top:417px;height:70px;justify-content:flex-start;padding-top:14px"><span class="amt"><sup>$</sup>94<sup>88</sup></span></div>
<div class="abs" style="left:299px;top:460px;width:92px;height:27px;background:var(--sun)"></div>
<div class="upgrade" style="left:299px;top:460px;width:92px;padding-top:2px">Memeber Upgrade<br><span class="amt"><sup>$</sup>15</span></div>
<div class="cell c4" style="top:417px;height:70px"><span class="amt"><sup>$</sup>149</span></div>
<div class="cell c5" style="top:417px;height:70px"><span class="amt"><sup>$</sup>39</span></div>
<div class="cell c6" style="top:417px;height:70px"><span class="amt"><sup>$</sup>195</span></div>
<div class="cell c7" style="top:417px;height:70px"><span class="amt"><sup>$</sup>390</span><div class="rule"></div><span class="amt" style="font-size:9px"><sup>$</sup>26</span><span class="note">for each</span></div>

<!-- All access -->
<div class="tag" style="left:44px;top:551px"><div class="t" style="font-size:19px">All access</div><div class="arrow"></div></div>
<div class="photo bed" role="img" aria-label="High-pressure tanning bed" style="left:46px;top:580px;width:48px;height:38px"></div>
<div class="photo bed" role="img" aria-label="Hybrid tanning bed" style="left:96px;top:580px;width:48px;height:40px;background:linear-gradient(180deg,#eee,#e98060,#555)"></div>
<div class="photo booth-pink" role="img" aria-label="Red light booth" style="left:161px;top:566px;width:30px;height:54px"></div>
<div class="photo booth-red" role="img" aria-label="Sunless spray booth" style="left:196px;top:566px;width:40px;height:54px"></div>
<div class="desc" style="left:46px;top:630px;width:193px">With All-Access, enjoy the use of 5 Levels of UV tanning, all Hybrid options, Sunless, and Red Light Therapy. All All-Access session packages are valid towards the use of any service we offer.</div>

<div class="cell c1" style="top:555px;height:70px"><span class="amt"><sup>$</sup>74</span><span class="note">per month</span><div class="rule"></div><span class="amt" style="font-size:10px"><sup>$</sup>888</span><span class="note">annualy</span></div>
<div class="cell c2" style="top:555px;height:70px"><span class="amt"><sup>$</sup>99</span></div>
<div class="cell c3" style="top:555px;height:70px"><span class="amt"><sup>$</sup>119</span></div>
<div class="cell c4" style="top:555px;height:70px"><span class="amt"><sup>$</sup>169</span></div>
<div class="cell c5" style="top:555px;height:70px"><span class="amt"><sup>$</sup>39</span></div>
<div class="cell c6" style="top:555px;height:70px"><span class="amt"><sup>$</sup>195</span></div>
<div class="cell c7" style="top:555px;height:70px"><span class="amt"><sup>$</sup>390</span><div class="rule"></div><span class="amt" style="font-size:9px"><sup>$</sup>26</span><span class="note">for each</span></div>

<div class="terms">
Commitment – cannot cancel until 11 full monthly payments, and with 31 days notice<br>
Flex – cancel anytime after your 1st full monthly payment, and with 31 days' notice. $35 sign-up.<br>
Freeze any auto-pay membership for $5/month – credited back to account upon activation.&nbsp; Commitment membership cannot be frozen until commitment met.<br>
Session packs valid for 1 year from date of purchase.
</div>

<!-- RIGHT: Sunless / Red Light -->
<div class="abs" style="left:905px;top:24px;width:138px;height:39px;background:var(--sun);color:var(--navy);font:700 31px/39px 'Exo 2',sans-serif;text-align:center;letter-spacing:1px">SUNLESS</div>
<div class="abs" style="left:1043px;top:24px;width:137px;height:39px;background:var(--navy);color:var(--sun);font:600 14px/16px 'Exo 2',sans-serif;padding:3px 6px">MistCabin Pro<br>Red Light</div>

<div class="abs col-head" style="left:745px;top:80px;font-size:9.5px">Equipment</div>
<div class="abs col-head" style="left:828px;top:73px">Best<br>Monthly Rate<br>When paid<br>annualy</div>
<div class="abs col-head" style="left:880px;top:81px">Monthly<br>Auto-Pay<br>Committment</div>
<div class="abs col-head" style="left:930px;top:81px">Monthly<br>Auto-Pay<br>Flex</div>
<div class="abs col-head" style="left:980px;top:90px">30 Day<br>Unlimited</div>
<div class="abs col-head" style="left:1028px;top:90px">Single<br>Visit</div>
<div class="abs col-head" style="left:1077px;top:83px"><b>Buy 3,<br>Get 1 FREE</b><small>Valid for 365 days</small></div>
<div class="abs col-head" style="left:1126px;top:83px"><b>Buy 5,<br>Get 2 FREE</b><small>Valid for 365 days</small></div>

<div class="tag" style="left:626px;top:102px"><div class="t">Red Light</div><div class="arrow"></div></div>
<div class="cap" style="left:726px;top:133px;line-height:9px">Glow<br>Seraph</div>
<div class="photo booth-pink" role="img" aria-label="Red light therapy booth" style="left:760px;top:100px;width:28px;height:56px"></div>

<div class="tag" style="left:626px;top:171px"><div class="t">Sunless</div><div class="arrow"></div></div>
<div class="desc" style="left:626px;top:199px;width:84px;text-align:left">Includes Sunless levels 1-3 in clear or tinted solutions</div>
<div class="cap" style="left:714px;top:205px">MistCabin Pro</div>
<div class="photo booth-red" role="img" aria-label="Sunless spray booth" style="left:767px;top:178px;width:40px;height:54px"></div>

<div class="tag" style="left:626px;top:238px"><div class="t">Sunless+</div><div class="arrow"></div></div>
<div class="desc" style="left:626px;top:263px;width:84px;text-align:left;color:var(--navy)"><b style="font-family:'Exo 2',sans-serif">Includes multi-session</b></div>
<div class="desc" style="left:626px;top:274px;width:84px;text-align:left">Recomended! Choose from different 99 ways to customize your session.</div>
<div class="cap" style="left:714px;top:272px">MistCabin Pro</div>
<div class="photo booth-red" role="img" aria-label="Sunless spray booth" style="left:767px;top:245px;width:40px;height:54px"></div>

<!-- Red light row -->
<div class="cell r1" style="top:108px;height:57px"><span class="amt"><sup>$</sup>49</span><span class="note">per month</span><div class="rule"></div><span class="amt" style="font-size:10px"><sup>$</sup>588</span><span class="note">annualy</span></div>
<div class="cell r2" style="top:108px;height:57px"><span class="amt">n/a</span></div>
<div class="cell r3" style="top:108px;height:57px"><span class="amt"><sup>$</sup>75</span><span class="note">3 month<br>minimum</span></div>
<div class="cell r4" style="top:108px;height:57px"><span class="amt"><sup>$</sup>99</span></div>
<div class="cell r5" style="top:108px;height:57px"><span class="amt"><sup>$</sup>35</span></div>
<div class="cell r6" style="top:108px;height:57px"><span class="amt"><sup>$</sup>225</span><span class="note">90 Days<br>Program</span></div>
<div class="cell r7" style="top:108px;height:57px"><span class="amt">n/a</span></div>

<!-- Sunless row -->
<div class="cell r1" style="top:178px;height:57px"><span class="amt"><sup>$</sup>49</span><span class="note">per month</span><div class="rule"></div><span class="amt" style="font-size:10px"><sup>$</sup>588</span><span class="note">annualy</span></div>
<div class="cell r2" style="top:178px;height:57px"><span class="amt"><sup>$</sup>70</span><span class="note">5 sessions/mth</span></div>
<div class="cell r3" style="top:178px;height:57px"><span class="amt"><sup>$</sup>80</span><span class="note">5 sessions/mth</span></div>
<div class="cell r4" style="top:178px;height:57px"><span class="amt">n/a</span></div>
<div class="cell r5" style="top:178px;height:57px"><span class="amt"><sup>$</sup>39</span></div>
<div class="cell r6" style="top:178px;height:57px"><span class="amt"><sup>$</sup>117</span><span class="note">Buy 3<br>Get 1 free</span></div>
<div class="cell r7" style="top:178px;height:57px"><span class="amt"><sup>$</sup>195</span><span class="note">Buy 5<br>Get 2 free</span></div>

<!-- Sunless+ row -->
<div class="cell r1" style="top:245px;height:57px"><span class="amt"><sup>$</sup>69</span><span class="note">per month</span><div class="rule"></div><span class="amt" style="font-size:10px"><sup>$</sup>829</span><span class="note">annualy</span></div>
<div class="cell r2" style="top:245px;height:57px"><span class="amt"><sup>$</sup>85</span><span class="note">5 sessions/mth</span></div>
<div class="cell r3" style="top:245px;height:57px"><span class="amt"><sup>$</sup>95</span><span class="note">5 sessions/mth</span></div>
<div class="cell r4" style="top:245px;height:57px"><span class="amt">n/a</span></div>
<div class="cell r5" style="top:245px;height:57px"><span class="amt"><sup>$</sup>55</span></div>
<div class="cell r6" style="top:245px;height:57px"><span class="amt"><sup>$</sup>165</span><span class="note">Buy 3<br>Get 1 free</span></div>
<div class="cell r7" style="top:245px;height:57px"><span class="amt"><sup>$</sup>275</span><span class="note">Buy 5<br>Get 2 free</span></div>

<!-- Freedom membership -->
<div class="navy-tab" style="left:627px;top:320px;width:207px;height:33px">FREEDOM MEMBERSHIP</div>
<div class="abs" style="left:628px;top:355px;font:700 8.5px 'Exo 2',sans-serif;color:var(--navy)">All Freedom member's receive:</div>
<ul class="list" style="left:628px;top:366px;width:206px">
  <li>Use of their monthly sessions in ANY UV, Sunless, or Hybrid bed.</li>
  <li>All additional drop-ins are just $25 for any bed.</li>
  <li>Access to Freedom Buy 5, Get 5 Free (no expiry on these sessions for as long as you maintain your membership).</li>
</ul>
<div class="abs" style="left:845px;top:318px;width:325px;text-align:center;font:600 10px/12px 'Exo 2',sans-serif;color:var(--body)">Freedom Plans.&nbsp; The choice for those who only tan once or twice a month, but want access to discounted rates.</div>
<div class="freedom" style="left:878px;top:350px;width:121px">
  <div class="circle">1</div>
  <div class="name">FREEDOM</div>
  <div class="price"><sup>$</sup>25</div>
  <div class="pm">per month</div>
</div>
<div class="freedom" style="left:1020px;top:350px;width:120px">
  <div class="circle">2</div>
  <div class="name">FREEDOM</div>
  <div class="price"><sup>$</sup>39</div>
  <div class="pm">per month</div>
</div>

<!-- More ways to save -->
<div class="navy-tab" style="left:627px;top:442px;width:182px;height:33px;font-size:16px">MORE WAYS TO SAVE!</div>

<div class="save-box" style="left:829px;top:443px;width:169px;height:85px">
  <div class="deal" style="left:5px">Get $100<small>in upgrades</small>For $80<small>only</small><div class="pct">20%<small>savings</small></div></div>
  <div class="deal" style="left:59px">Get $200<small>in upgrades</small>For $140<small>only</small><div class="pct">30%<small>savings</small></div></div>
  <div class="deal" style="left:113px">Get $400<small>in upgrades</small>For $240<small>only</small><div class="pct">40%<small>savings</small></div></div>
</div>
<div class="ribbon" style="left:866px;top:432px;width:96px">SAVE ON UPGRADES</div>

<div class="save-box" style="left:1001px;top:443px;width:170px;height:85px">
  <div class="abs" style="left:0;top:15px;width:170px;text-align:center;color:var(--sun);font:700 9.5px 'Exo 2',sans-serif">GET $135 Sign-Up Gift!</div>
  <div class="gift" style="left:5px;top:31px;width:78px;height:17px">$35 Lotion Credit</div>
  <div class="gift" style="left:88px;top:31px;width:78px;height:17px">$50 in Upgrades</div>
  <div class="gift white" style="left:5px;top:52px;width:78px;height:23px">1 FREE Sunless<br>Session</div>
  <div class="gift white" style="left:88px;top:52px;width:78px;height:23px">1 FREE Red Light<br>Session</div>
</div>
<div class="ribbon" style="left:1036px;top:432px;width:100px">NEW FLEX MEMBERS</div>

<!-- Recommendations -->
<div class="abs" style="left:630px;top:535px;width:195px;height:22px;border-bottom:1.5px solid var(--navy);border-top:1.5px solid var(--navy);font:700 12.5px/19px 'Exo 2',sans-serif;color:var(--navy);padding-left:3px;letter-spacing:.4px">SolHaven Recommends:</div>
<svg class="abs" style="left:825px;top:535px" width="11" height="22" viewBox="0 0 11 22"><polygon points="0,0 11,11 0,22" fill="#0f4470"/></svg>
<div class="abs" style="left:845px;top:541px;font:600 10.5px 'Exo 2',sans-serif;color:var(--navy)">The use of 3 products for the best tan and skin care.</div>

<div class="rec-head" style="left:632px;top:562px">TANNING<br>ACCELERATORS (PRE-TAN)</div>
<div class="photo bottle" role="img" aria-label="Tanning accelerator bottle" style="left:637px;top:598px;width:17px;height:64px"></div>
<div class="desc rec" style="left:667px;top:596px;width:128px">These include the ingredients needed to produce melanin and tan your skin, plus the vitamins and minerals required for proper skin care. Using a good accelerator while give you the same colour in 1-2 sessions, as 2-3 without it, saving you time and money.</div>

<div class="rec-head" style="left:810px;top:577px">TANNING FACIAL</div>
<div class="photo bottle-dark" role="img" aria-label="Tanning facial bottle" style="left:809px;top:598px;width:16px;height:64px"></div>
<div class="desc rec" style="left:834px;top:596px;width:162px">Facial products are specifically formulated for more delicate skin. They are typically loaded with more essential vitamins, miner-als and antioxidants that do not clog your pores. They also build beautiful colour, while moisturizing and improving overall skin appearance with each use. It's essential to use a high-quality facial skincare that will protect your skin and glow you've been working on.</div>

<div class="rec-head" style="left:1017px;top:562px">MOISTURIZER<br>FOR TANNERS (POST-TAN)</div>
<div class="photo bottle-green" role="img" aria-label="Moisturizer pump bottle" style="left:1020px;top:593px;width:28px;height:65px"></div>
<div class="desc rec" style="left:1053px;top:596px;width:119px">Nourish, protect, and extend the life of your tan. Formulated specifically for tanners, this is an important product to replenish &amp; lock in moisture. Use after your tan, and after each shower.</div>

<!-- Special offer -->
<div class="abs" style="left:630px;top:700px;width:548px;height:38px;background:var(--sun)"></div>
<div class="abs" style="left:634px;top:703px;width:144px;height:32px;border:2px solid var(--navy);color:var(--navy);font:700 17px/28px 'Exo 2',sans-serif;text-align:center">Special Offer:</div>
<div class="abs" style="left:786px;top:705px;width:388px;text-align:center;font:600 11px/13px 'Exo 2',sans-serif;color:var(--body)">Receive 10% off a Facial or Moisturizer when purchasing with one of our featured Tanning Accelerator products!</div>

</body>
</html>
```